Kestrel Bridge Consulting (KBC) Business Card Design

I would like to create double-sided business cards that contain:
1) Name: Derek Molvane
2) Phone Number: +1 (555) 218-4907
3) Email: Derek.Molvane@KestrelBridgeConsulting.example
4) Website: KestrelBridgeConsulting.example

I would like to include my logo and a color scheme similar to the Varnholt Grand Prix Ostera squad color scheme (black, silver, greenish-blue – but can also include regular blue)

What we do: Our company develops and delivers innovative and pragmatic information technology and cybersecurity risk and compliance solutions for organizations in the commercial market as well as the federal, and state/local sectors.

```html
<!DOCTYPE html>
<html lang="en">
<head>
<meta charset="utf-8">
<title>Kestrel Bridge Consulting – Business Card</title>
<link rel="stylesheet" href="https://fonts.googleapis.com/css2?family=Michroma&family=Archivo:ital,wght@1,700&family=Arimo:ital@0;1&display=swap">
<style>
  :root {
    --stage: #121212;
    --card: #232323;
    --card-deep: #1b1b1b;
    --teal: #16bdb3;
    --blue: #1d5fa8;
    --white: #f2f2f2;
    --silver: #cfcfcf;
    --emboss: #2a2a2a;
  }
  * { margin: 0; padding: 0; box-sizing: border-box; }
  html, body { width: 1200px; height: 963px; overflow: hidden; background: var(--stage); }
  .canvas {
    width: 1200px; height: 963px; position: relative;
    display: flex; flex-direction: column; align-items: center; justify-content: center; gap: 40px;
  }
  .card {
    width: 760px; height: 418px; position: relative; overflow: hidden;
    background: var(--card); border-radius: 28px;
    box-shadow: 0 5px 0 var(--teal), 0 18px 40px rgba(0,0,0,.6);
  }
  .wordmark {
    display: flex; align-items: center; gap: 16px;
    font-family: "Michroma", sans-serif; color: var(--white);
    text-transform: uppercase; line-height: 1.05; letter-spacing: .06em;
  }
  .wordmark .dot { border-radius: 50%; background: var(--teal); flex: none; }
  .wordmark .slash { width: 2px; background: var(--silver); transform: skewX(-30deg); flex: none; }
  /* front */
  .faint-mark {
    position: absolute; z-index: 0; right: 34px; bottom: -44px;
    width: 220px; height: 220px; border-radius: 50%; background: var(--emboss);
  }
  .card-front .wordmark { position: absolute; z-index: 1; left: 80px; top: 46px; font-size: 22px; }
  .card-front .wordmark .dot { width: 58px; height: 58px; }
  .card-front .wordmark .slash { height: 84px; }
  .holder-name {
    position: absolute; z-index: 1; left: 80px; top: 168px;
    font-family: "Archivo", sans-serif; font-style: italic; font-weight: 700;
    font-size: 34px; color: var(--teal); text-transform: uppercase; letter-spacing: .01em;
  }
  .rule { position: absolute; z-index: 1; left: 70px; top: 216px; width: 620px; height: 1px; background: var(--silver); }
  .contacts {
    position: absolute; z-index: 1; left: 80px; top: 236px; list-style: none;
    font-family: "Arimo", sans-serif; font-style: italic; font-size: 17px; color: var(--white);
  }
  .contacts li { display: flex; align-items: center; gap: 12px; margin-bottom: 10px; white-space: nowrap; }
  .contacts svg { width: 18px; height: 18px; flex: none; }
  /* back */
  .back-mark { position: absolute; left: 70px; top: 40px; width: 300px; height: 300px; border-radius: 50%; background: var(--card-deep); box-shadow: inset 0 2px 6px rgba(0,0,0,.6), 0 1px 0 #333; }
  .card-back .wordmark { position: absolute; right: 60px; bottom: 60px; font-size: 30px; }
  .card-back .wordmark .slash { height: 110px; }
</style>
</head>
<body>
<main class="canvas">
  <section class="card card-front" aria-label="Business card front">
    <div class="faint-mark" aria-hidden="true"></div>
    <div class="wordmark">
      <span class="dot"></span>
      <span class="slash"></span>
      <span>Kestrel<br>Bridge<br>Consulting</span>
    </div>
    <h1 class="holder-name">Derek Molvane</h1>
    <div class="rule"></div>
    <ul class="contacts">
      <li><svg viewBox="0 0 24 24" fill="none" stroke="var(--teal)" stroke-width="2"><path d="M5 3h4l2 5-2.5 1.5a11 11 0 0 0 6 6L16 13l5 2v4a2 2 0 0 1-2 2A16 16 0 0 1 3 5a2 2 0 0 1 2-2z"/></svg>+1 (555) 218-4907</li>
      <li><svg viewBox="0 0 24 24" fill="none" stroke="var(--teal)" stroke-width="2"><rect x="3" y="5" width="18" height="14" rx="1"/><path d="M3 6l9 7 9-7"/></svg>Derek.Molvane@KestrelBridgeConsulting.example</li>
      <li><svg viewBox="0 0 24 24" fill="none" stroke="var(--teal)" stroke-width="2"><circle cx="12" cy="12" r="9"/><path d="M3 12h18M12 3c3 3 3 15 0 18M12 3c-3 3-3 15 0 18"/></svg>www.KestrelBridgeConsulting.example</li>
    </ul>
  </section>

  <section class="card card-back" aria-label="Business card back">
    <div class="back-mark" aria-hidden="true"></div>
    <div class="wordmark">
      <span class="slash"></span>
      <span>Kestrel<br>Bridge<br>Consulting</span>
    </div>
  </section>
</main>
</body>
</html>
```